bramwick.link bramwick.space bramwick.press website

The website is named BRAMWICK and it will have 3 domain names. bramwick.link, press, space.
I'd like it to be viewed on Pads, pcs and phones.

page menu:

bramwick.link(start page): presentation of company. (creative, design, app, new product innovation.)
Here we'll need sosial media icons: vextro, pollumax, gorvida, tenkoral. (light but some 'fruity' colors)

bramwick.press: blog. It will be a 75% picture blog > rest will be text. I need to be able to resize pictures and shape columns to picture size. (light but some 'fruity' colors)

bramwick.space : the fun part of this web design, however, on entering the page I'd like a non-disclosure agreement where viewer simply click "yes, I agree" after filling out contact info. (check attached document)
We will have space here for uploading PDF files viewers can download. There is also a blog space here to tell in brief about the PDF file. (maybe a space/sci-fi theme her e.g spacechimp, Vessa the space dog?)

I will attach the logo here I want you to use > and develop for the .space .press webpage. The logo i uploaded is for the .link page.

Target Market(s)

venture capitalists

Number of Pages Required

3 page

Requirements
Must have
• a few 'fruity colors' but mostly white and grey

```html
<!DOCTYPE html>
<html lang="en">
<head>
<meta charset="utf-8">
<title>Bramwick Link</title>
<link href="https://fonts.googleapis.com/css2?family=Varela+Round&family=Arimo:wght@400;700&family=Open+Sans:ital,wght@1,600&display=swap" rel="stylesheet">
<style>
:root{
  --green:#569a3c;
  --green-dark:#2f6e2b;
  --green-title:#2d7a32;
  --red:#e2472f;
  --red-band:#df5240;
  --pink:#fadcdc;
  --ink:#222;
  --body:#333;
  --rule:#e3e3e3;
  --white:#fff;
}
*{margin:0;padding:0;box-sizing:border-box}
html,body{width:858px;height:1200px;overflow:hidden;background:var(--white)}
body{position:relative;font-family:"Arimo",Arial,sans-serif;color:var(--body)}
.abs{position:absolute}

/* header */
.topbar{left:0;top:0;width:858px;height:26px}
.contact{top:6px;font-size:11px;color:#444;display:flex;align-items:center;gap:6px}
.contact-mail{left:463px}
.contact-phone{left:605px}
.social{left:716px;top:5px;display:flex;gap:5px}
.social span{font-size:8px;color:var(--white);background:var(--red);padding:3px 2px;border-radius:1px;line-height:1}
.brand{left:64px;top:14px;font-family:"Varela Round",sans-serif;font-size:20px;color:var(--ink);letter-spacing:1px}
.brand-mark{left:64px;top:40px;width:22px;height:22px;background:var(--red)}
.nav{left:450px;top:26px;display:flex;height:30px;align-items:center;font-size:11px;color:#333}
.nav a{color:inherit;text-decoration:none;height:30px;line-height:30px;padding:0 18px;position:relative}
.nav a+a::before{content:"";position:absolute;left:0;top:11px;height:8px;border-left:1px solid #ccc}
.nav .active{background:var(--green);color:var(--white);width:65px;text-align:center;padding:0}
.nav-rule{left:0;top:56px;width:858px;height:1px;background:#ddd}

/* hero */
.hero{left:0;top:69px;width:858px;height:384px;background:linear-gradient(180deg,#6f97c4 0%,#a9c4de 45%,#e8d9b8 72%,#3a3a3a 100%)}
.hero-caption{left:0;top:418px;width:858px;height:35px;background:rgba(30,30,30,.75);color:var(--white);font-size:15.5px;text-align:center;line-height:35px}
.arrow{top:223px;width:24px;height:24px;background:#3a3a3a;border:1px solid #888}

/* headings */
.title{left:0;width:858px;text-align:center;font-family:"Varela Round",sans-serif;font-size:23px;color:var(--green-title)}
.title em{font-style:normal;color:var(--red)}
.rule{left:288px;width:290px;height:1px;background:var(--rule)}
.rule-accent{left:408px;width:49px;height:3px;background:var(--green)}

.intro{left:68px;top:542px;width:728px;font-size:11px;line-height:16px;text-align:center;color:var(--body)}
.intro p+p{margin-top:6px}
.read-more{left:0;top:642px;width:858px;text-align:center;font-size:9.5px;font-weight:700;color:var(--ink);text-decoration:underline}

.band{left:0;top:697px;width:858px;height:122px;background:linear-gradient(180deg,#e45a45,#d84a37)}
.band-text{left:0;top:725px;width:858px;text-align:center;font-family:"Open Sans",sans-serif;font-style:italic;font-weight:600;font-size:19px;line-height:34px;color:var(--white);text-shadow:0 1px 2px rgba(0,0,0,.3)}

/* services */
.service{top:920px;width:186px;text-align:center}
.service h3{font-weight:400;font-size:13.5px;color:var(--ink);margin-top:8px}
.service p{font-size:10px;line-height:16px;margin-top:8px;color:var(--body)}
.service svg{display:block;margin:0 auto}
.service.featured h3,.service.featured p{color:var(--white)}
.feature-bg{left:242px;top:907px}

/* footer */
.footer{left:0;top:1130px}
.copyright{left:63px;top:1170px;font-size:8px;color:var(--white)}
.footer-brand{left:703px;top:1146px;font-family:"Varela Round",sans-serif;font-size:16px;color:var(--ink);letter-spacing:1px}
</style>
</head>
<body>

<svg class="abs topbar" width="858" height="26" aria-hidden="true"><polygon points="262,0 858,0 858,26 234,26" fill="var(--pink)"/></svg>
<div class="abs contact contact-mail">
  <svg width="12" height="9"><rect x="0.5" y="0.5" width="11" height="8" fill="var(--red)"/><polyline points="0.5,0.5 6,5 11.5,0.5" fill="none" stroke="#fff" stroke-width="1"/></svg>
  sales@bramwick.link</div>
<div class="abs contact contact-phone">
  <svg width="16" height="16"><circle cx="8" cy="8" r="7" fill="none" stroke="var(--red)" stroke-width="1.3"/><path d="M5 4 L7 6 L6 7 Q7 9 9 10 L10 9 L12 11 L10.5 12.5 Q6 11.5 3.5 5.5 Z" fill="var(--red)"/></svg>
  (555) 014 2290</div>
<div class="abs social"><span>gorvida</span><span>vextro</span><span>glimora</span><span>tenkoral</span></div>

<div class="abs brand">BRAMWICK</div>
<div class="abs brand-mark"></div>

<nav class="abs nav">
  <a class="active">Home</a><a>About</a><a>Services</a><a>Our Work</a><a>Contact</a>
</nav>
<div class="abs nav-rule"></div>

<div class="abs hero" role="img" aria-label="Photo of business people silhouetted against a sunrise with sketched technology icons and gears overhead"></div>
<div class="abs arrow" style="left:4px"><svg width="22" height="22"><polyline points="13,7 9,11 13,15" fill="none" stroke="#fff" stroke-width="2"/></svg></div>
<div class="abs arrow" style="left:829px"><svg width="22" height="22"><polyline points="9,7 13,11 9,15" fill="none" stroke="#fff" stroke-width="2"/></svg></div>
<div class="abs hero-caption">Lorem Ipsum Dolor Sit Amet Consectetuer Adipiscing Elit Sed Diam Nonummy Nibh</div>

<h1 class="abs title" style="top:485px">Welcome to <em>Bramwick Link</em></h1>
<div class="abs rule" style="top:524px"></div>
<div class="abs rule-accent" style="top:523px"></div>

<div class="abs intro">
  <p>Lorem ipsum dolor sit amet, consectetuer adipiscing elit, sed diam nonummy nibh euismod tincidunt ut laoreet dolore magna aliquam erat volutpat. Ut wisi enim ad minim veniam, quis nostrud exerci tation ullamcorper suscipit lobortis nisl ut aliquip ex ea commodo consequat. Duis autem vel eum iriure dolor in hendrerit in vulputate velit esse molestie consequat, vel illum dolore eu feugiat nulla facilisis at vero eros et accumsan et iusto odio dignissim qui blandit praesent luptatum zzril delenit augue duis dolore te feugait nulla facilisi.</p>
  <p>We are committed to providing our customers with quality products, designs and 100% Work Satisfaction</p>
</div>
<div class="abs read-more">Read More</div>

<div class="abs band" role="img" aria-label="Red tinted photo of an office with people working"></div>
<div class="abs band-text">We Strive To Out Work Our Competition With An Effective Approach And A Powerful<br>Skill Set, Which Is Why Were Industry Leading.</div>

<h2 class="abs title" style="top:834px">Our <em>Services</em></h2>
<div class="abs rule" style="top:866px"></div>
<div class="abs rule-accent" style="top:865px"></div>

<svg class="abs feature-bg" width="186" height="196" aria-hidden="true"><polygon points="0,0 155,0 186,31 186,196 31,196 0,165" fill="var(--green)"/></svg>

<div class="abs service" style="left:52px">
  <svg width="86" height="86"><circle cx="43" cy="43" r="41" fill="#fff" stroke="var(--green)" stroke-width="2.5"/><circle cx="43" cy="43" r="35" fill="var(--green)"/><circle cx="43" cy="35" r="5" fill="#fff"/><path d="M30 55 Q43 42 56 55 Z" fill="#fff"/></svg>
  <h3>Creative</h3><p>Lorem ipsum dolor sit amet, consectetuer adipiscing elit, sed diam nonummy nibh.</p>
</div>
<div class="abs service featured" style="left:242px">
  <svg width="86" height="86"><circle cx="43" cy="43" r="41" fill="none" stroke="var(--green-dark)" stroke-width="2.5"/><circle cx="43" cy="43" r="35" fill="var(--green-dark)"/><rect x="32" y="30" width="16" height="22" rx="2" fill="none" stroke="#fff" stroke-width="2"/><rect x="46" y="38" width="9" height="16" rx="1.5" fill="#fff"/></svg>
  <h3>App Development</h3><p>Lorem ipsum dolor sit amet, consectetuer adipiscing elit, sed diam nonummy nibh.</p>
</div>
<div class="abs service" style="left:440px">
  <svg width="86" height="86"><circle cx="43" cy="43" r="41" fill="#fff" stroke="var(--green)" stroke-width="2.5"/><circle cx="43" cy="43" r="35" fill="var(--green)"/><circle cx="36" cy="34" r="5" fill="none" stroke="#fff" stroke-width="2.5" stroke-dasharray="2.5 1.5"/><circle cx="47" cy="31" r="4" fill="none" stroke="#fff" stroke-width="2" stroke-dasharray="2 1.5"/><path d="M40 58 L40 50 Q36 44 42 40 Q54 38 54 48 L52 52 L50 52 L50 58 Z" fill="#fff"/></svg>
  <h3>New Product Innovations</h3><p>Lorem ipsum dolor sit amet, consectetuer adipiscing elit, sed diam nonummy nibh.</p>
</div>
<div class="abs service" style="left:630px">
  <svg width="86" height="86"><circle cx="43" cy="43" r="41" fill="#fff" stroke="var(--green)" stroke-width="2.5"/><circle cx="43" cy="43" r="35" fill="var(--green)"/><rect x="28" y="30" width="30" height="20" fill="none" stroke="#fff" stroke-width="2"/><line x1="38" y1="56" x2="48" y2="56" stroke="#fff" stroke-width="2"/><line x1="43" y1="50" x2="43" y2="56" stroke="#fff" stroke-width="2"/><line x1="38" y1="44" x2="52" y2="30" stroke="#fff" stroke-width="2.5"/></svg>
  <h3>Design</h3><p>Lorem ipsum dolor sit amet, consectetuer adipiscing elit, sed diam nonummy nibh.</p>
</div>

<svg class="abs footer" width="858" height="70" aria-hidden="true">
  <polygon points="0,27 648,27 668,5 858,5 858,70 0,70" fill="var(--red)"/>
  <polyline points="0,26 648,26 668,4 858,4" fill="none" stroke="var(--green)" stroke-width="3"/>
</svg>
<div class="abs copyright">Copyright© 2016 &nbsp;Bramwick Link &nbsp;All rights reserved</div>
<div class="abs footer-brand">BRAMWICK</div>

</body>
</html>
```